Webbanner-Design für Informatik Dienstleistungen und Webdesign
Zielgruppe
Informatik Dienstleistungen und Webdesign
Aufgabenstellung
Es soll immer das gleiche Gesicht auf den Banner und ein kurzer Satz.
1. Sie haben das Business - wir die Software
2. Sie haben Anforderungen - wir Lösungen
3. Sie brauchen Unterstützung - wir helfen
Die Banner sollen auf unserer Homepage www.varmek-design.ch auf der Startseite durchlaufen. Das Format soll 1200x500 Pixel sein

```html
<!DOCTYPE html>
<html lang="de">
<head>
<meta charset="utf-8">
<title>Webbanner – Informatik Dienstleistungen</title>
<link rel="stylesheet" href="https://fonts.googleapis.com/css2?family=Nunito+Sans:wght@300;800&display=swap">
<style>
  :root {
    --page-bg: #ffffff;
    --banner-bg: #1b2029;
    --banner-bg-deep: #13161d;
    --grid-line: rgba(70, 130, 175, 0.10);
    --grid-tint: rgba(40, 90, 130, 0.45);
    --band-blue: #1f78c8;
    --band-blue-light: #2d92de;
    --glow: #3fd6ff;
    --line-blue: #2d7fc4;
    --text-white: #ffffff;
    --photo-hair: #a48a63;
    --photo-skin: #c3a07c;
    --photo-teal: #3aa7ad;
    --photo-dark: #15181e;
  }
  html, body {
    margin: 0;
    padding: 0;
    width: 910px;
    height: 1200px;
    overflow: hidden;
    background: var(--page-bg);
  }
  .sheet {
    position: relative;
    width: 910px;
    height: 1200px;
  }
  .banner {
    position: absolute;
    left: 42px;
    width: 826px;
    height: 343px;
    overflow: hidden;
    background:
      repeating-linear-gradient(90deg, var(--grid-line) 0 1px, transparent 1px 9px),
      repeating-linear-gradient(0deg, var(--grid-line) 0 1px, transparent 1px 9px),
      radial-gradient(ellipse 30% 28% at 22% 18%, var(--grid-tint) 0%, transparent 70%),
      radial-gradient(ellipse 38% 30% at 30% 92%, var(--grid-tint) 0%, transparent 70%),
      radial-gradient(ellipse 22% 25% at 62% 85%, rgba(40, 90, 130, 0.3) 0%, transparent 70%),
      linear-gradient(180deg, var(--banner-bg) 0%, var(--banner-bg-deep) 100%);
  }
  .banner--business { top: 52px; }
  .banner--requirements { top: 437px; }
  .banner--support { top: 820px; }

  .signal-lines {
    position: absolute;
    left: 0;
    bottom: 0;
    width: 420px;
    height: 120px;
  }
  .portrait {
    position: absolute;
    right: 0;
    top: 0;
    width: 380px;
    height: 343px;
    background:
      radial-gradient(ellipse 24% 30% at 42% 38%, var(--photo-skin) 0%, rgba(195,160,124,0.6) 50%, transparent 100%),
      radial-gradient(ellipse 30% 58% at 70% 52%, rgba(58,167,173,0.65) 0%, transparent 100%),
      radial-gradient(ellipse 50% 75% at 52% 30%, var(--photo-hair) 0%, rgba(164,138,99,0.55) 55%, transparent 100%),
      linear-gradient(180deg, transparent 60%, var(--photo-dark) 100%),
      linear-gradient(90deg, rgba(21,24,30,0) 0%, var(--photo-dark) 22%, var(--photo-dark) 100%);
  }
  .band {
    position: absolute;
    left: 0;
    top: 121px;
    width: 519px;
    height: 74px;
    background: linear-gradient(90deg, var(--band-blue) 0%, var(--band-blue) 82%, var(--band-blue-light) 100%);
  }
  .band::after {
    content: "";
    position: absolute;
    right: -45px;
    top: -40px;
    width: 90px;
    height: 154px;
    background: radial-gradient(ellipse at center, rgba(63,214,255,0.75) 0%, rgba(63,214,255,0.25) 40%, transparent 70%);
  }
  .slogan {
    position: absolute;
    top: 7px;
    margin: 0;
    font-family: "Nunito Sans", sans-serif;
    font-weight: 300;
    font-size: 31px;
    line-height: 30px;
    color: var(--text-white);
    white-space: nowrap;
  }
  .slogan strong { font-weight: 800; }
  .slogan .line { display: block; }
  .banner--business .slogan { left: 62px; }
  .banner--business .line--answer { padding-left: 126px; }
  .banner--requirements .slogan { left: 77px; }
  .banner--requirements .line--answer { padding-left: 56px; }
  .banner--support .slogan { left: 51px; }
  .banner--support .line--answer { padding-left: 95px; }
</style>
</head>
<body>
<main class="sheet">

  <section class="banner banner--business">
    <svg class="signal-lines" viewBox="0 0 420 120" aria-hidden="true">
      <g stroke="#2d7fc4" stroke-width="1" fill="none">
        <line x1="68" y1="120" x2="68" y2="86"/><circle cx="68" cy="84" r="2"/>
        <line x1="94" y1="120" x2="94" y2="53"/><circle cx="94" cy="51" r="2"/>
        <line x1="148" y1="120" x2="148" y2="12"/><circle cx="148" cy="10" r="2"/>
        <line x1="160" y1="120" x2="160" y2="28"/><circle cx="160" cy="26" r="2"/>
        <line x1="211" y1="120" x2="211" y2="30"/><circle cx="211" cy="28" r="2"/>
        <line x1="260" y1="120" x2="260" y2="33"/><circle cx="260" cy="31" r="2"/>
        <line x1="284" y1="120" x2="284" y2="46"/><circle cx="284" cy="44" r="2"/>
        <line x1="312" y1="120" x2="312" y2="92"/><circle cx="312" cy="90" r="2"/>
      </g>
    </svg>
    <div class="portrait" role="img" aria-label="Porträtfoto einer lächelnden jungen Frau mit langen blonden Haaren in schwarzem Sportshirt, türkis angeleuchtet"></div>
    <div class="band">
      <p class="slogan">
        <span class="line">Sie haben das <strong>Business</strong></span>
        <span class="line line--answer">- wir die <strong>Software</strong></span>
      </p>
    </div>
  </section>

  <section class="banner banner--requirements">
    <svg class="signal-lines" viewBox="0 0 420 120" aria-hidden="true">
      <g stroke="#2d7fc4" stroke-width="1" fill="none">
        <line x1="68" y1="120" x2="68" y2="86"/><circle cx="68" cy="84" r="2"/>
        <line x1="94" y1="120" x2="94" y2="53"/><circle cx="94" cy="51" r="2"/>
        <line x1="148" y1="120" x2="148" y2="12"/><circle cx="148" cy="10" r="2"/>
        <line x1="160" y1="120" x2="160" y2="28"/><circle cx="160" cy="26" r="2"/>
        <line x1="211" y1="120" x2="211" y2="30"/><circle cx="211" cy="28" r="2"/>
        <line x1="260" y1="120" x2="260" y2="33"/><circle cx="260" cy="31" r="2"/>
        <line x1="284" y1="120" x2="284" y2="46"/><circle cx="284" cy="44" r="2"/>
        <line x1="312" y1="120" x2="312" y2="92"/><circle cx="312" cy="90" r="2"/>
      </g>
    </svg>
    <div class="portrait" role="img" aria-label="Porträtfoto einer lächelnden jungen Frau mit langen blonden Haaren in schwarzem Sportshirt, türkis angeleuchtet"></div>
    <div class="band">
      <p class="slogan">
        <span class="line">Sie haben <strong>Anforderungen</strong></span>
        <span class="line line--answer">- wir <strong>Lösungen</strong></span>
      </p>
    </div>
  </section>

  <section class="banner banner--support">
    <svg class="signal-lines" viewBox="0 0 420 120" aria-hidden="true">
      <g stroke="#2d7fc4" stroke-width="1" fill="none">
        <line x1="68" y1="120" x2="68" y2="86"/><circle cx="68" cy="84" r="2"/>
        <line x1="94" y1="120" x2="94" y2="53"/><circle cx="94" cy="51" r="2"/>
        <line x1="148" y1="120" x2="148" y2="12"/><circle cx="148" cy="10" r="2"/>
        <line x1="160" y1="120" x2="160" y2="28"/><circle cx="160" cy="26" r="2"/>
        <line x1="211" y1="120" x2="211" y2="30"/><circle cx="211" cy="28" r="2"/>
        <line x1="260" y1="120" x2="260" y2="33"/><circle cx="260" cy="31" r="2"/>
        <line x1="284" y1="120" x2="284" y2="46"/><circle cx="284" cy="44" r="2"/>
        <line x1="312" y1="120" x2="312" y2="92"/><circle cx="312" cy="90" r="2"/>
      </g>
    </svg>
    <div class="portrait" role="img" aria-label="Porträtfoto einer lächelnden jungen Frau mit langen blonden Haaren in schwarzem Sportshirt, türkis angeleuchtet"></div>
    <div class="band">
      <p class="slogan">
        <span class="line">Sie brauchen <strong>Unterstützung</strong></span>
        <span class="line line--answer">- <strong>wir helfen</strong></span>
      </p>
    </div>
  </section>

</main>
</body>
</html>
```